KVT bottled water label

We are from The KVT Corner (TKC) - a university campus-retail initiative. As part of our branding exercise, we would like to produce a new range of bottled water and need a new label design carrying the following headline: "U Make A Different U" (primary headline) with "The World Is Your Campus" as the sub-headline (secondary headline).
Usage Of Line:
Emphasis must be given to the primary headline, and must not be placed before or on top of the primary headline. The reader must first read the primary headline before reading the secondary headline (assuming the reader reads from left to right and top to bottom.)
THE CONCEPT BEHIND OUR LINE:
Some Background:
Perceived as a fast-rising star since our inception in 2000, Pelrow Enterprise College challenged the Singapore education landscape - long dominated by an established field of long-tenured universities – by providing a holistic, broad-based and cross-disciplinary form of education that incorporates global exposure, internships and networking opportunities to prepare our students for real-world challenges - an experiential learning environment which we’ve proudly pioneered. Watch these videos from our graduates sharing their KVT experiences: http://kvt.example/22
When our first batch of graduates started their careers in 2004, employers saw a different breed of leaders. The graduates from KVT were bold, confident, articulate, versatile, well-rounded and eager for challenges. Today, more than 10,000 graduates across the world are testament to our trademark holistic and interactive approach to education. Our graduate employment record has been, and continues to be, robust with 60% finding jobs before graduation, and close to 100% getting employed within six months of graduation. Watch employers from Zentrik, QLV, RMO & HJK at: http://kvt.example/21
That is why we invite prospective students to Discover A Different 'U' - the letter 'U' can be interpreted to mean the 'U'niversity or 'U' as an individual (the prospective student).
The New Line:
With our new headline "U Make A Different U - The World Is Your Campus", we now pose the challenge back to our prospective students, and invite them to make a difference. How different their university experience can be, and how much they can be transformed, is limited only by their imagination.
For more information on KVT, please visit our website at: kvt.example.edu
Design:
The design must be vibrant and fresh to appeal to our students (from 18 years of age), yet still fit in perfectly on a table for a board of professionals and executive directors.
Audience:
It should appeal to the general masses, from our students to distinguished guests and executive directors to KVT.
Things to include (Requirements):
1. KVT logo (as below) must be included)
https://files.example.net/s/qq41wd/KVT%20Formal%20Logo.zip
2. Only 4 colours can be used (white is considered one color)
3. Must design within perimeters of working file:
https://files.example.net/s/pp73rk/bottled%20water%20working%20file.pdf
References
http://kvt.example/1m
http://kvt.example/1o
http://kvt.example/1p
http://kvt.example/1q
http://kvt.example/1r
http://kvt.example/1s
http://kvt.example/1t
http://kvt.example/1u
http://kvt.example/1v
http://kvt.example/1w
http://kvt.example/1x
http://kvt.example/1y

```html
<!DOCTYPE html>
<html lang="en">
<head>
<meta charset="utf-8">
<title>KVT Bottled Water Label</title>
<link rel="stylesheet" href="https://fonts.googleapis.com/css2?family=Russo+One&family=Orbitron:wght@500&family=Arimo:wght@400;700&display=swap">
<style>
  :root {
    --blue-mid: #2a9be6;
    --blue-light: #4fb6f2;
    --blue-edge: #1676c4;
    --blue-deep: #0a2f6b;
    --white: #ffffff;
    --ink: #1b1b1b;
  }
  html, body { margin: 0; padding: 0; overflow: hidden; background: var(--white); }
  .label {
    position: relative;
    width: 1200px; height: 248px; overflow: hidden;
    background:
      linear-gradient(180deg, var(--blue-edge) 0, var(--blue-mid) 14px, var(--blue-light) 50%, var(--blue-mid) 234px, var(--blue-edge) 248px);
    font-family: "Arimo", Arial, sans-serif;
  }
  .brand {
    position: absolute; left: 240px; top: 50px;
    display: flex; align-items: center; gap: 10px;
    font-family: "Russo One", sans-serif; font-size: 40px; line-height: 1; color: var(--blue-deep);
  }
  .brand-square { width: 22px; height: 22px; background: var(--blue-deep); }
  .headline {
    position: absolute; left: 68px; top: 176px; margin: 0;
    font-family: "Russo One", sans-serif; font-weight: 400; font-size: 42px; line-height: 1;
    letter-spacing: 1px; color: var(--blue-deep);
    white-space: nowrap;
  }
  .subheadline {
    position: absolute; left: 128px; top: 220px; margin: 0;
    font-family: "Orbitron", sans-serif; font-weight: 500; font-size: 18px; line-height: 1;
    color: var(--blue-deep); white-space: nowrap;
  }
  .info-panel {
    position: absolute; left: 910px; top: 6px; width: 280px; height: 236px;
    background: var(--white); box-sizing: border-box; padding: 8px 10px;
    color: var(--ink); font-size: 7px; line-height: 1.3;
  }
  .product-name { font-size: 10px; font-weight: 700; margin: 2px 0 6px; }
  .nutrition { width: 160px; border-collapse: collapse; font-size: 6.5px; }
  .nutrition td, .nutrition th { border: 0.6px solid var(--ink); padding: 0 3px; text-align: left; font-weight: 400; }
  .nutrition .title th { font-weight: 700; font-size: 7.5px; }
  .nutrition .num { text-align: right; }
  .note { margin: 3px 0 0; width: 170px; }
  .maker { margin: 5px 0 0; width: 170px; }
  .tech { margin: 6px 0 0; font-weight: 700; font-size: 7.5px; }
  .tech-name { font-size: 20px; font-weight: 700; letter-spacing: 0.5px; line-height: 1; margin-top: 1px; }
  .tech-place { font-size: 8px; margin-left: 70px; }
</style>
</head>
<body>
<div class="label">
  <div class="brand"><span class="brand-square"></span>KVT</div>
  <h1 class="headline">U MAKE A DIFFERENT U</h1>
  <p class="subheadline">The World Is Your Campus</p>

  <section class="info-panel">
    <p class="product-name">Oxygenated Drinking Water</p>
    <table class="nutrition">
      <tr class="title"><th colspan="3">Nutrition Information</th></tr>
      <tr><td colspan="3">Serving per package : 500ml</td></tr>
      <tr><td colspan="3">Serving size : 100ml</td></tr>
      <tr><td></td><td class="num">per serving</td><td class="num">per 100ml</td></tr>
      <tr><td>energy</td><td class="num">0 kcal*</td><td class="num">0 kcal*</td></tr>
      <tr><td>protein</td><td class="num">0 g</td><td class="num">0 g</td></tr>
      <tr><td>total fat</td><td class="num">0 g</td><td class="num">0 g</td></tr>
      <tr><td>carbohydrate</td><td class="num">0 g</td><td class="num">0 g</td></tr>
      <tr><td>sodium</td><td class="num">0 mg</td><td class="num">0 mg</td></tr>
    </table>
    <p class="note">* 1 kcal = 4.2kJ<br>Not a significant source of dietary fibre, saturated fats and cholesterol</p>
    <p class="maker">Manufactured in Singapore for<br>AQUALORE WATERWORKS (S) PTE LTD<br>TEL: 65 6000 1234 &nbsp; FAX: 65 6000 5678<br>EMAIL: info@aqualore.example</p>
    <p class="tech">Produced Using The Technology of</p>
    <div class="tech-name">AQUALORE</div>
    <div class="tech-place">singapore</div>
  </section>
</div>
</body>
</html>
```